Letterhead design x 2, follower page, with compliments slip and envelope design X 2

Design letterhead x 2, follower page, with compliments slip and envelope x 2 for Harbor Venture Partners, a business broking company. Using the colours of the existing logo and a white background for a clean, sophisticated look.

Target Market(s)

Family Business owners and regular business owners looking to buy or sell their business, or improve the value of their business.

Font styles to use
Sans Serif

Requirements
Must have
• Letterhead design 1 - Additional logos for Crale Business Sales, NTQR and DWL to be included in a small size somewhere on the page. Crale Business Sales logo only to have the wording 'Powered By' alongside. Please do not distort the size of the logos.
Letterhead design 2 - Additional logos for NTQR and DWL to be included in a small size somewhere on the page. This design will not include the Crale Business Sales logo or the words 'Powered By'. Please do not distort the size of the logos.
Envelope design 1 - Please include an address window
Envelope design 2 - Do not include an address window

```html
<!DOCTYPE html>
<html lang="en">
<head>
<meta charset="utf-8">
<title>Harbor Venture Partners – Stationery</title>
<link rel="stylesheet" href="https://fonts.googleapis.com/css2?family=Lato:wght@400;700&display=swap">
<style>
  :root{
    --orange:#f05a28;
    --grey:#939aa1;
    --ink:#222;
    --text:#555;
    --rule:#c9c9c9;
    --bg:#eceeef;
    --paper:#fff;
  }
  *{box-sizing:border-box;margin:0;padding:0}
  html,body{width:1200px;height:1200px;overflow:hidden}
  body{background:var(--bg);font-family:"Lato",sans-serif;color:var(--text);position:relative}
  .sheet{position:absolute;background:var(--paper);overflow:hidden;box-shadow:0 2px 8px rgba(0,0,0,.12)}
  .sheet svg.corners{position:absolute;inset:0;width:100%;height:100%}
  .abs{position:absolute}

  /* Letterhead */
  .letterhead{left:40px;top:215px;width:600px;height:771px}
  .brand-mark{position:absolute;border:2px solid var(--grey);border-radius:50%}
  .brand-name{position:absolute;color:var(--orange);font-weight:700;line-height:1}
  .letterhead .brand-mark{left:59px;top:32px;width:44px;height:44px}
  .letterhead .brand-name{left:113px;top:33px;font-size:15px}
  .letterhead .brand-name span{display:block;margin-bottom:1px}
  .header-rule{left:187px;top:53px;width:362px;height:1px;background:var(--orange)}
  .contact{left:306px;top:24px;font-size:11px;color:var(--ink);line-height:14px}
  .contact .row{display:flex;align-items:center;gap:4px;white-space:nowrap}
  .contact svg{width:9px;height:9px;fill:var(--orange)}
  .contact .gap{margin-left:8px}
  .contact .address{margin-top:4px;font-size:11.5px;line-height:16px}
  .contact .web em{font-style:normal;color:var(--orange)}
  .letter{left:57px;top:139px;width:485px;font-size:9.5px;line-height:11.5px;color:#444}
  .letter .meta{margin-bottom:12px}
  .letter .salutation{margin:28px 0 22px}
  .letter p.body{line-height:17.3px;margin-bottom:17px;text-align:justify}
  .signoff{left:57px;top:524px;font-size:9.5px;color:#444}
  .signature{left:57px;top:543px;width:140px;height:18px;background:linear-gradient(90deg,#d8d8d8,#eee)}
  .signer{left:57px;top:569px;font-size:12px;color:var(--ink)}
  .signer-title{left:57px;top:589px;font-size:9.5px;color:#444}
  .powered{left:59px;top:688px;font-size:10px;color:var(--orange);letter-spacing:.2px}
  .footer-rule{left:139px;top:694px;width:410px;height:1px;background:var(--rule)}
  .partner{position:absolute;color:#333;font-weight:700}
  .partner.crale{left:60px;top:710px;font-size:10px;line-height:11px;letter-spacing:1px}
  .badge{left:157px;top:705px;width:60px;height:60px;border-radius:50%;border:2px solid #203a80}
  .partner.ntqr{left:235px;top:732px;font-size:11px;color:#1f3b7a;letter-spacing:1.5px}

  /* Envelope front */
  .env-front{left:720px;top:400px;width:440px;height:220px}
  .env-front .brand-mark{left:23px;top:15px;width:35px;height:35px}
  .env-front .brand-name{left:64px;top:15px;font-size:11.5px}
  .env-front .brand-name span{display:block}
  .env-rule{left:25px;top:186px;width:388px;height:1px;background:var(--orange)}
  .env-address{left:25px;top:193px;font-size:8px;color:var(--ink)}

  /* Envelope back */
  .env-back{left:720px;top:655px;width:440px;height:216px}
  .env-back .flap{position:absolute;left:0;top:0;width:440px;height:52px}
  .env-back .faint-name{left:0;right:0;top:118px;text-align:center;font-size:16px;font-weight:700;color:#f1e3dd}
</style>
</head>
<body>

<section class="sheet letterhead" aria-label="Letterhead">
  <svg class="corners" viewBox="0 0 600 771" preserveAspectRatio="none" aria-hidden="true">
    <path d="M0 0 H92 Q12 32 0 115 Z" fill="var(--orange)"/>
    <path d="M600 640 Q592 752 480 771 H600 Z" fill="var(--grey)"/>
  </svg>

  <div class="brand-mark" aria-hidden="true"></div>
  <div class="brand-name"><span>Harbor</span><span>Venture</span><span>Partners</span></div>
  <div class="abs header-rule"></div>

  <div class="abs contact">
    <div class="row">
      <svg viewBox="0 0 10 10"><path d="M1 3c0-2 8-2 8 0v1H7V3H3v1H1zM2 5h6l1 4H1z"/></svg>08 5550 1428
      <svg class="gap" viewBox="0 0 10 10"><path d="M2 0h6v10H2zM3 1v7h4V1z"/></svg>0400 555 219
    </div>
    <div class="row">
      <svg viewBox="0 0 10 10"><path d="M0 2h10v6H0zM1 3l4 3 4-3"/></svg>info@harborventurepartners.com.au
    </div>
    <div class="address">Unit 4, 18 Kestrel Way, Margate Bay, WA, 6290</div>
    <div class="web">www.<em>harborventurepartners</em>.com.au</div>
  </div>

  <div class="abs letter">
    <div class="meta">Issuing Date: May 5, 2018</div>
    <div>Name Of Employee Mr. XYZABC<br>Address of Employee<br>Address Line 2 etc..</div>
    <div class="salutation">Dear Mr.XYZABC</div>
    <p class="body">Lorem Ipsum has been the industry's standard dummy text ever since the 1500s, when an unknown printer took a galley of type and scrambled it to make a type specimen book. It has survived not only five centuries, but also the leap into electronic typesetting, remaining essentially unchanged. It was popularised in the 1960s with the release of Letraset sheets containing Lorem Ipsum passages, and more recently with desktop publishing software like Aldus PageMaker including versions of Lorem Ipsum.</p>
    <p class="body">Lorem Ipsum is simply dummy text of the printing and typesetting industry. Lorem Ipsum has been the industry's standard dummy text ever since the 1500s, when an unknown printer took a galley of type and scrambled it to make a type specimen book.</p>
    <p class="body">It has survived not only five centuries, but also the leap into electronic typesetting, remaining essentially unchanged. It was popularised in the 1960s with the release of Letraset sheets containing Lorem Ipsum passages.</p>
  </div>

  <div class="abs signoff">Yours Sincerely</div>
  <div class="abs signature" role="img" aria-label="Handwritten signature of Daniel Marsh"></div>
  <div class="abs signer">Daniel Marsh</div>
  <div class="abs signer-title">Managing Director</div>

  <div class="abs powered">POWERED BY</div>
  <div class="abs footer-rule"></div>
  <div class="partner crale">CRALE<br>BUSINESS<br>SALES</div>
  <div class="abs badge" role="img" aria-label="DWL advisor member badge"></div>
  <div class="partner ntqr">NTQR</div>
</section>

<section class="sheet env-front" aria-label="Envelope front">
  <svg class="corners" viewBox="0 0 440 220" preserveAspectRatio="none" aria-hidden="true">
    <path d="M0 0 H48 Q8 18 0 60 Z" fill="var(--orange)"/>
    <path d="M440 180 Q436 212 396 220 H440 Z" fill="var(--grey)"/>
  </svg>
  <div class="brand-mark" aria-hidden="true"></div>
  <div class="brand-name"><span>Harbor</span><span>Venture</span><span>Partners</span></div>
  <div class="abs env-rule"></div>
  <div class="abs env-address">Unit 4, 18 Kestrel Way, Margate Bay, WA, 6290</div>
</section>

<section class="sheet env-back" aria-label="Envelope back">
  <svg class="flap" viewBox="0 0 440 52" aria-hidden="true">
    <path d="M0 0 H440 L422 52 H16 Z" fill="var(--orange)"/>
  </svg>
  <div class="abs faint-name">Harbor Venture Partners</div>
</section>

</body>
</html>
```